Local Horticulturalist needs Business card design

Meridel Horticulture would like to update our existing business card and utilize our new logo (design attached)....we specialize in getting the best out of our customers yard with professional maintenance programs, expert pruning and hedging and garden restorations.
Utilizing colors from attached logo I would like a design that implies professionalism and if possible our businesses love of restoration through plants.
I also sometimes write down for my customers a start date and price on the back of my current card
Target Market(s)
Home owners
Contractors
Industry/Entity Type
Gardener
Contact Information for Business Card
Gareth Volkstrom | Horticulturalist
ph: 0438275946
meridelhort@fernmail.example
www.meridelhorticulture.example.au
Requirements
Must have
- crucial information easy to read
- incorporate current logo
- Horticulturalist listed preferably near name
Nice to have
- currently I write a job start date and price on the back of my current card so something that integrates this would be beneficial
Should not have
- be pretty or flowerey
- be too white or basic

```html
<!DOCTYPE html>
<html lang="en">
<head>
<meta charset="utf-8">
<title>Meridel Horticulture – Business Card</title>
<link rel="stylesheet" href="https://fonts.googleapis.com/css2?family=Open+Sans:wght@400;600;700&display=swap">
<style>
  :root {
    --leaf-green: #7cc242;
    --leaf-green-dark: #5fa62c;
    --bark-brown: #7d6b57;
    --soil-grey: #6f655b;
    --card-white: #ffffff;
    --backdrop: #e9e6e1;
  }
  html, body {
    margin: 0;
    width: 1200px;
    height: 900px;
    overflow: hidden;
    background: var(--backdrop);
    font-family: "Open Sans", Arial, sans-serif;
  }
  .stage {
    position: relative;
    width: 1200px;
    height: 900px;
  }
  .card {
    position: absolute;
    width: 620px;
    height: 354px;
    border-radius: 20px;
    background: var(--card-white);
    overflow: hidden;
    box-shadow: 0 6px 18px rgba(60, 45, 30, 0.18);
  }
  .card--front { left: 130px; top: 80px; }
  .card--back  { left: 450px; top: 470px; }
  .card__wave {
    position: absolute;
    inset: 0;
    width: 100%;
    height: 100%;
  }
  .brand {
    position: absolute;
    display: flex;
    align-items: center;
    gap: 14px;
  }
  .brand__dot {
    width: 58px;
    height: 58px;
    border-radius: 50%;
    background: var(--leaf-green);
    flex: none;
  }
  .brand__name {
    margin: 0;
    font-weight: 700;
    font-size: 30px;
    line-height: 1;
    color: var(--leaf-green);
    letter-spacing: 0.2px;
  }
  .brand__tagline {
    margin: 4px 0 0;
    font-weight: 600;
    font-size: 15px;
    color: var(--bark-brown);
    letter-spacing: 0.6px;
  }
  .card--front .brand { left: 60px; top: 120px; }
  .card--back .brand { left: 34px; top: 30px; }
  .card--back .brand__dot { width: 50px; height: 50px; }
  .card--back .brand__name { font-size: 25px; }
  .card--back .brand__tagline { font-size: 13px; }

  .person {
    position: absolute;
    right: 34px;
    top: 102px;
    width: 360px;
    text-align: right;
    border-bottom: 2px solid var(--leaf-green);
    padding-bottom: 3px;
  }
  .person__name {
    margin: 0;
    font-weight: 700;
    font-size: 26px;
    line-height: 1.1;
    color: var(--leaf-green);
  }
  .person__role {
    margin: 0;
    font-size: 14px;
    color: var(--soil-grey);
  }
  .contact {
    position: absolute;
    left: 34px;
    top: 184px;
    width: 320px;
    margin: 0;
    padding: 6px 0 0;
    list-style: none;
    border-top: 2px solid var(--leaf-green);
  }
  .contact__item {
    display: flex;
    align-items: center;
    gap: 12px;
    font-size: 15px;
    line-height: 23px;
    color: var(--leaf-green);
    white-space: nowrap;
  }
  .contact__icon {
    width: 13px;
    height: 13px;
    flex: none;
    fill: none;
    stroke: var(--soil-grey);
    stroke-width: 1.6;
  }
</style>
</head>
<body>
<main class="stage">

  <section class="card card--front" aria-label="Card front">
    <svg class="card__wave" viewBox="0 0 620 354" preserveAspectRatio="none" aria-hidden="true">
      <defs>
        <linearGradient id="greenBandFront" x1="0" y1="0" x2="1" y2="0">
          <stop offset="0" stop-color="#6fb83a"/>
          <stop offset="1" stop-color="#8fd051"/>
        </linearGradient>
      </defs>
      <path d="M0,354 L0,318 C180,316 400,290 620,206 L620,354 Z" fill="url(#greenBandFront)"/>
      <path d="M0,300 C180,298 400,272 620,186" fill="none" stroke="#7d6b57" stroke-width="6"/>
    </svg>
    <div class="brand">
      <span class="brand__dot"></span>
      <div>
        <p class="brand__name">Meridel Horticulture</p>
        <p class="brand__tagline">Garden Restorations &amp; Maintenance</p>
      </div>
    </div>
  </section>

  <section class="card card--back" aria-label="Card back">
    <svg class="card__wave" viewBox="0 0 620 354" preserveAspectRatio="none" aria-hidden="true">
      <defs>
        <linearGradient id="greenBandBack" x1="0" y1="0" x2="1" y2="0">
          <stop offset="0" stop-color="#6fb83a"/>
          <stop offset="1" stop-color="#8fd051"/>
        </linearGradient>
      </defs>
      <path d="M0,354 L0,328 C200,321 380,301 470,276 C560,251 600,231 620,206 L620,354 Z" fill="url(#greenBandBack)"/>
      <path d="M0,314 C200,307 380,287 470,262 C560,237 600,217 620,192" fill="none" stroke="#7d6b57" stroke-width="6"/>
    </svg>

    <div class="brand">
      <span class="brand__dot"></span>
      <div>
        <p class="brand__name">Meridel Horticulture</p>
        <p class="brand__tagline">Garden Restorations &amp; Maintenance</p>
      </div>
    </div>

    <div class="person">
      <p class="person__name">Gareth Volkstrom</p>
      <p class="person__role">Horticulturalist</p>
    </div>

    <ul class="contact">
      <li class="contact__item">
        <svg class="contact__icon" viewBox="0 0 14 14" aria-hidden="true"><path d="M3 1.5 L5 4 L4 5.5 C5 7.5 6.5 9 8.5 10 L10 9 L12.5 11 L11 12.8 C6 12 2 8 1.2 3 Z"/></svg>
        0438275946
      </li>
      <li class="contact__item">
        <svg class="contact__icon" viewBox="0 0 14 14" aria-hidden="true"><rect x="1" y="3" width="12" height="8"/><path d="M1 3 L7 8 L13 3"/></svg>
        meridelhort@fernmail.example
      </li>
      <li class="contact__item">
        <svg class="contact__icon" viewBox="0 0 14 14" aria-hidden="true"><circle cx="7" cy="7" r="5.8"/><path d="M1.2 7 H12.8 M7 1.2 C4.5 4 4.5 10 7 12.8 M7 1.2 C9.5 4 9.5 10 7 12.8"/></svg>
        www.meridelhorticulture.example.au
      </li>
    </ul>
  </section>

</main>
</body>
</html>
```